Awards Banquet Invitation

The Cedar Bluff Area Chamber of Commerce is celebrating it's 65th year at our Annual Awards Banquet (business leader awards). Since we were founded in 1950, we will have a 1950's theme. Dress will be 1950's Formal. I don't want cheesy 1950's. I want Classic feel and fonts from that era. This event is for business professionals so looks from ads in the 50's would be good for inspiration. I would like a look that I can use for the program and event ads. Invitation will include an RSVP insert. Date: February 10, 2015. Time: 6 cocktails, 7 dinner & program, Location: Holm Weide Country Club. Dress is 1950's formal

Target Market(s)

Business owners - our members

Industry/Entity Type

Business

Other font styles liked:
• Lasalle, linotype, thirsty

Colors
86cfc6
474747
ffffff
000000

Requirements
Must have
• classic 50's font and old-fashioned feel
Should not have
• sock hop, soda fountain, 50's diner

```html
<!DOCTYPE html>
<html lang="en">
<head>
<meta charset="utf-8">
<title>Annual Awards Banquet Invitation</title>
<link rel="stylesheet" href="https://fonts.googleapis.com/css2?family=Fontdiner+Swanky&family=Lobster&family=Tinos&family=Yanone+Kaffeesatz:wght@500;600&family=Yellowtail&display=swap">
<style>
  :root {
    --teal: #86cfc6;
    --teal-deep: #5fb3a9;
    --charcoal: #474747;
    --white: #ffffff;
    --black: #000000;
    --red: #c41e26;
    --cream: #fcfae6;
    --backdrop: #ece8e1;
  }
  * { margin: 0; padding: 0; box-sizing: border-box; }
  html, body { width: 1200px; height: 853px; overflow: hidden; }
  body { background: var(--backdrop); position: relative; }

  .card { position: absolute; background: var(--white); box-shadow: 0 6px 18px rgba(0,0,0,.18); overflow: hidden; }
  .card svg.card-art { position: absolute; inset: 0; }
  .card .line { position: absolute; left: 0; right: 0; text-align: center; white-space: nowrap; }

  /* Invitation */
  .invitation { left: 130px; top: 96px; width: 440px; height: 660px; }
  .invite-lead { top: 118px; font: 13px "Tinos", serif; color: var(--charcoal); letter-spacing: .3px; }
  .invite-lead sup { font-size: 8px; }
  .invite-host { top: 150px; font: 17px "Fontdiner Swanky", cursive; color: var(--black); }
  .invite-host small { font-size: 10px; }
  .invite-title { top: 178px; font: 60px/1 "Lobster", cursive; color: var(--red); }
  .invite-title-2 { top: 248px; }
  .invite-details { position: absolute; left: 34px; top: 480px; font-family: "Yanone Kaffeesatz", sans-serif; color: var(--black); }
  .invite-date { font-size: 32px; font-weight: 600; line-height: 1.2; }
  .invite-venue { font-size: 28px; font-weight: 500; margin-top: 6px; }
  .invite-extras { font-size: 19px; font-weight: 500; margin-top: 6px; }
  .invite-extras .dot { color: var(--red); }

  /* RSVP */
  .rsvp { left: 620px; top: 330px; width: 450px; height: 370px; }
  .rsvp-title { top: 34px; font: 86px/1 "Fontdiner Swanky", cursive; color: var(--red); }
  .rsvp-prompt { top: 134px; font: 14px "Fontdiner Swanky", cursive; color: var(--black); }
  .rsvp-date { top: 168px; font: 600 34px/1 "Yanone Kaffeesatz", sans-serif; color: var(--black); }
  .rsvp-field { position: absolute; left: 110px; font: 600 19px "Yanone Kaffeesatz", sans-serif; color: var(--black); display: flex; align-items: flex-end; gap: 6px; }
  .rsvp-field .rule { display: block; height: 1px; background: var(--black); margin-bottom: 4px; }
  .rsvp-field-name { top: 232px; }
  .rsvp-field-name .rule { width: 215px; }
  .rsvp-field-guest { top: 258px; }
  .rsvp-field-guest .rule { width: 195px; }
  .rsvp-choice { position: absolute; top: 296px; display: flex; align-items: center; gap: 8px; font: 13px "Yellowtail", cursive; color: var(--black); }
  .rsvp-choice .bubble { width: 24px; height: 24px; border-radius: 50%; background: var(--teal); }
  .rsvp-accept { left: 90px; }
  .rsvp-decline { left: 240px; }
</style>
</head>
<body>

<section class="card invitation" aria-label="Invitation">
  <svg class="card-art" width="440" height="660" viewBox="0 0 440 660">
    <rect width="440" height="660" fill="var(--teal)" role="img" aria-label="Teal band with retro boomerang pattern"/>
    <rect x="10" y="10" width="420" height="640" fill="none" stroke="var(--white)" stroke-width="2" stroke-dasharray="5 4"/>
    <path d="M0 95 C80 78 160 92 205 108 Q220 98 235 108 C300 88 380 66 440 62 L440 420 C380 408 300 410 235 424 Q220 414 205 424 C160 440 80 448 0 448 Z"
          fill="var(--white)" stroke="var(--charcoal)" stroke-width="3"/>
    <path d="M0 470 L380 450 L425 428 L372 528 L440 602 L0 602 Z" fill="var(--cream)"/>
    <path d="M380 450 L425 428 L405 470 Z" fill="var(--teal-deep)"/>
    <circle cx="40" cy="120" r="14" fill="var(--teal)" opacity=".5" role="img" aria-label="Atomic starburst ornament"/>
    <circle cx="405" cy="142" r="12" fill="var(--teal)" opacity=".5" role="img" aria-label="Atomic starburst ornament"/>
  </svg>
  <p class="line invite-lead">Please join us as we celebrate our 65<sup>th</sup> anniversary</p>
  <p class="line invite-host"><small>The</small> Cedar Bluff Chamber of Commerce</p>
  <h1 class="line invite-title">Annual Awards</h1>
  <p class="line invite-title invite-title-2">Banquet</p>
  <div class="invite-details">
    <p class="invite-date">February 10, 2015</p>
    <p class="invite-venue">at the Holm Weide Country Club</p>
    <p class="invite-extras">50s Formal Attire <span class="dot">•</span> 6 cocktails, 7 dinner &amp; program</p>
  </div>
</section>

<section class="card rsvp" aria-label="RSVP card">
  <svg class="card-art" width="450" height="370" viewBox="0 0 450 370">
    <path d="M140 0 L450 0 L450 30 C380 40 300 44 245 40 Q230 32 215 40 C190 30 160 12 140 0 Z"
          fill="var(--teal)" stroke="var(--charcoal)" stroke-width="3"/>
    <path d="M0 330 C100 324 180 330 215 340 Q230 330 245 340 C300 345 370 355 450 368 L450 370 L0 370 Z"
          fill="var(--teal)" stroke="var(--charcoal)" stroke-width="3"/>
    <path d="M70 172 L380 172 L395 190 L380 220 L70 220 L80 196 Z" fill="var(--cream)"/>
    <path d="M70 220 L380 220 L380 225 L70 225 Z" fill="#b8b8b8"/>
    <circle cx="28" cy="36" r="14" fill="var(--teal)" opacity=".5" role="img" aria-label="Atomic starburst ornament"/>
    <circle cx="420" cy="200" r="12" fill="var(--teal)" opacity=".5" role="img" aria-label="Atomic starburst ornament"/>
  </svg>
  <h2 class="line rsvp-title">RSVP</h2>
  <p class="line rsvp-prompt">Please respond by</p>
  <p class="line rsvp-date">February 10, 2015</p>
  <p class="rsvp-field rsvp-field-name">M <span class="rule"></span></p>
  <p class="rsvp-field rsvp-field-guest">Guest <span class="rule"></span></p>
  <p class="rsvp-choice rsvp-accept"><span class="bubble"></span>accepts with pleasure</p>
  <p class="rsvp-choice rsvp-decline"><span class="bubble"></span>declines with regrets</p>
</section>

</body>
</html>
```